Security company needs a business card design

We have a logo & we provide security services specialising in the construction site industry & remote areas. We are looking for a modern design preferably hi-tech as we provide hi-end specialised security services. We do not do pubs, clubs etc. Many of our employees are ex defence force & are highly qualified in covert ops etc.

Below are details that we would like on the front of the business card (I have attached our logo)
Logo + ML 736204918 (ML is abbreviation for "Master License")
We are also members of "TRVOK" not sure if we need to put their logo on the business card or just make a reference to our membership (please advise - I have also attached their logo)

Company name: Bluegate Security Services Pty Ltd

1) Employee name: Gordon Haskell
Designation: Security Advisor / Director
Contact: M: 0471 583 904
e:gordon@bluegatesecurityservices.com.au (500cards 1st order)
2) Employee name: Trevor Haskell
Designation: Manager
Contact: M: 0456 302 817
e:trevor@bluegatesecurityservices.com.au (250cards 1st order)
3) a generic card with no employee name or designation (250cards 1st order)

Company Address: 312 Wendell Rd, Marrowbank NSW 2483
T: +61 2 6690 4135 F: +61 2 6690 4172
E:admin@bluegatesecurityservices.com.au
www.bluegatesecurityservices.com.au

Below are details we provide which have been placed previously on the back of our business card:
Static Guards; Mobile Vehicle patrols; Alarm monitoring; 3 G CCTV Monitoring; Specialists in providing security requirements for construction sites & remote areas.
Updates

                                        Refer new pdf just uploaded

Target Market(s)

Security required for construction sites & remote areas

Industry/Entity Type

Construction

```html
<!DOCTYPE html>
<html lang="en">
<head>
<meta charset="utf-8">
<title>Bluegate Security Services – Business Card</title>
<link rel="stylesheet" href="https://fonts.googleapis.com/css2?family=Exo+2:wght@600;700&family=Didact+Gothic&display=swap">
<style>
  :root {
    --page: #b9b9bb;
    --blue-deep: #1f3596;
    --red: #e8231f;
    --navy-text: #24307e;
    --ink: #2b2b2e;
    --rule: #b9b9bb;
    --badge: #6f8c2c;
    --badge-ring: #e9d64a;
  }
  * { margin: 0; padding: 0; box-sizing: border-box; }
  html, body { width: 1200px; height: 900px; overflow: hidden; }
  body {
    background: var(--page);
    font-family: "Didact Gothic", sans-serif;
    color: var(--ink);
    position: relative;
  }
  .card {
    position: absolute;
    width: 520px;
    height: 316px;
    top: 292px;
    box-shadow: 0 6px 18px rgba(0,0,0,.25);
    overflow: hidden;
  }
  .card--front { left: 50px; }
  .card--back { left: 630px; }
  .card__bg { position: absolute; inset: 0; width: 100%; height: 100%; }
  .card__content { position: absolute; inset: 0; text-align: center; }

  /* Front */
  .brand {
    position: absolute;
    top: 44px; left: 0; right: 0;
    display: flex; align-items: center; justify-content: center; gap: 8px;
  }
  .brand__dot { width: 16px; height: 16px; border-radius: 50%; background: var(--blue-deep); }
  .brand__name {
    font-family: "Exo 2", sans-serif; font-weight: 700;
    font-size: 30px; color: var(--blue-deep); letter-spacing: .5px;
  }
  .licence { position: absolute; top: 90px; left: 0; right: 0; font-size: 9px; }
  .person__name {
    position: absolute; top: 112px; left: 0; right: 0;
    font-family: "Exo 2", sans-serif; font-weight: 700;
    font-size: 31px; color: var(--red); letter-spacing: 1px;
  }
  .person__role { position: absolute; top: 150px; left: 0; right: 0; font-size: 12px; color: var(--navy-text); }
  .contact {
    position: absolute; top: 176px; left: 0; right: 0;
    font-size: 11.5px; line-height: 16px;
  }
  .contact__label { color: var(--red); }
  .contact__rule { width: 260px; height: 1px; background: var(--rule); margin: 4px auto; }
  .member-badge {
    position: absolute; top: 268px; left: 252px;
    width: 16px; height: 16px; border-radius: 50%;
    background: var(--badge); border: 2px solid var(--badge-ring);
  }

  /* Back */
  .services__title {
    position: absolute; top: 30px; left: 0; right: 0;
    font-family: "Exo 2", sans-serif; font-weight: 700;
    font-size: 19px; color: var(--red); letter-spacing: .5px;
  }
  .services__list {
    position: absolute; top: 62px; left: 0; right: 0;
    list-style: none; font-size: 12px; line-height: 14px;
  }
  .services__gap { height: 10px; }
  .speciality { position: absolute; top: 232px; left: 0; right: 0; color: var(--navy-text); }
  .speciality__intro { font-size: 10.5px; letter-spacing: .5px; }
  .speciality__focus { font-family: "Exo 2", sans-serif; font-weight: 700; font-size: 15px; }
  .website { position: absolute; top: 278px; left: 0; right: 0; font-size: 13px; }
</style>
</head>
<body>

<svg width="0" height="0" style="position:absolute" aria-hidden="true">
  <defs>
    <linearGradient id="sides" x1="0" y1="0" x2="1" y2="0">
      <stop offset="0" stop-color="#3ba6e6"/>
      <stop offset=".25" stop-color="#1f3596"/>
      <stop offset=".5" stop-color="#7a7fa8"/>
      <stop offset=".72" stop-color="#f07a6e"/>
      <stop offset="1" stop-color="#e8231f"/>
    </linearGradient>
    <radialGradient id="face" cx=".5" cy=".45" r=".6">
      <stop offset="0" stop-color="#efeeec"/>
      <stop offset="1" stop-color="#d9d8d6"/>
    </radialGradient>
  </defs>
</svg>

<section class="card card--front">
  <svg class="card__bg" viewBox="0 0 520 316" aria-hidden="true">
    <rect width="520" height="316" fill="url(#sides)"/>
    <ellipse cx="262" cy="170" rx="246" ry="250" fill="#ffffff" opacity=".55"/>
    <ellipse cx="262" cy="170" rx="236" ry="240" fill="#c7c7c9"/>
    <ellipse cx="262" cy="170" rx="226" ry="232" fill="url(#face)"/>
  </svg>
  <div class="card__content">
    <div class="brand"><span class="brand__dot"></span><span class="brand__name">Bluegate</span></div>
    <p class="licence">ML 736204918</p>
    <h1 class="person__name">DORIAN WELSBY</h1>
    <p class="person__role">Security Advisor / Director</p>
    <div class="contact">
      <p><span class="contact__label">M:</span> +61 471 583 904 &nbsp;<span class="contact__label">E:</span> dorian@bluegatesecurityservices.com.au</p>
      <div class="contact__rule"></div>
      <p>312 WENDELL RD, MARROWBANK NSW 2483</p>
      <p><span class="contact__label">T:</span> +61 2 6690 4135 <span class="contact__label">F:</span> +61 2 6690 4172</p>
      <p><span class="contact__label">E:</span> admin@bluegatesecurityservices.com.au</p>
    </div>
    <span class="member-badge"></span>
  </div>
</section>

<section class="card card--back">
  <svg class="card__bg" viewBox="0 0 520 316" aria-hidden="true">
    <rect width="520" height="316" fill="url(#sides)"/>
    <ellipse cx="262" cy="165" rx="246" ry="250" fill="#ffffff" opacity=".55"/>
    <ellipse cx="262" cy="165" rx="236" ry="240" fill="#c7c7c9"/>
    <ellipse cx="262" cy="165" rx="226" ry="232" fill="url(#face)"/>
  </svg>
  <div class="card__content">
    <h2 class="services__title">BLUEGATE SECURITY SERVICES</h2>
    <ul class="services__list">
      <li>Static Guards</li>
      <li>Mobile Vehicle Patrols</li>
      <li>Foot Patrols</li>
      <li>Tactical Operations</li>
      <li>Call Outs</li>
      <li class="services__gap"></li>
      <li>Live 3G IP/IR Systems</li>
      <li>Hunting Cams</li>
      <li>Alarm Monitoring / Responce</li>
      <li>Asset Protection (GPS Tracking)</li>
      <li>Security Brief &amp; Incident Reporting</li>
    </ul>
    <div class="speciality">
      <p class="speciality__intro">WE SPECIALISE IN</p>
      <p class="speciality__focus">CONSTRUCTION SITE &amp; REMOTE AREAS</p>
    </div>
    <p class="website">www.bluegatesecurityservices.com.au</p>
  </div>
</section>

</body>
</html>
```